To create online free mini games website. There’re will be up to 100 games on website with 6-8 categories. Domain name is not selected yet.

Number of Pages Required

1 page

```html
<!DOCTYPE html>
<html lang="en">
<head>
<meta charset="utf-8">
<title>Tobin-Games</title>
<link href="https://fonts.googleapis.com/css2?family=Passion+One:wght@400;700&family=Oswald:wght@600;700&family=Exo+2:ital,wght@1,800&family=Montserrat:wght@600&family=Roboto:ital,wght@0,500;1,400&display=swap" rel="stylesheet">
<style>
:root{
  --stripe-a:#f4f4f4;
  --stripe-b:#c9c9c9;
  --blue-top:#02609a;
  --blue-bottom:#001d36;
  --orange:#f2a000;
  --orange-dark:#c96f00;
  --panel-dark:#2a2a2a;
  --panel-red:#8a1200;
  --panel-green:#1d8d12;
  --thumb:#999999;
  --tag:#7ecdc6;
  --ink:#2b2b2b;
  --white:#ffffff;
}
*{box-sizing:border-box;margin:0;padding:0}
html,body{width:1127px;height:1200px;overflow:hidden}
body{position:relative;font-family:"Roboto",sans-serif;
  background:repeating-linear-gradient(135deg,var(--stripe-a) 0 3px,var(--stripe-b) 3px 4px)}
.page-body{position:absolute;left:0;top:105px;width:1127px;height:1042px;
  background:linear-gradient(180deg,var(--blue-top),#004675 45%,var(--blue-bottom))}
.abs{position:absolute}
.logo{left:205px;top:26px;font-family:"Passion One",sans-serif;font-weight:700;font-size:50px;letter-spacing:2px;color:#3a3a3a;line-height:1}
.btn{height:30px;width:116px;border-radius:5px;background:linear-gradient(var(--orange),var(--orange-dark));
  border:2px solid #fff3c4;box-shadow:0 2px 3px rgba(0,0,0,.4);font-family:"Passion One",sans-serif;font-size:15px;
  color:#1a1a1a;display:flex;align-items:center;justify-content:center;text-transform:uppercase;font-style:italic}
.slider{left:204px;top:105px;width:711px;height:272px;overflow:hidden;
  background:radial-gradient(circle at 25% 30%,#c94fd6,transparent 45%),radial-gradient(circle at 75% 40%,#7fae3a,transparent 35%),linear-gradient(120deg,#5a2a9a,#7d3bb8 40%,#3b2a7a 70%,#5b2d8c)}
.slider-panel{left:145px;top:0;width:341px;height:177px;background:rgba(255,255,255,.22);padding:20px 24px}
.slider-title{font-family:"Oswald",sans-serif;font-weight:700;font-size:34px;color:#fff;line-height:1}
.slider-text{margin-top:10px;font-family:"Oswald",sans-serif;font-weight:600;font-size:10.5px;line-height:1.35;color:#fff;text-transform:uppercase}
.play{left:258px;top:135px;width:116px;height:30px;border-radius:4px;border:2px solid #fff;background:linear-gradient(#f04a17,#c01f00);
  font-family:"Exo 2",sans-serif;font-style:italic;font-weight:800;font-size:16px;color:#fff;display:flex;align-items:center;justify-content:center}
.dot{top:252px;width:32px;height:14px;border-radius:3px;background:#fff}
.dot.active{background:transparent;border:1px solid #fff}
.nav{left:205px;top:399px;width:566px;height:31px;border-radius:4px;border:2px solid #fff;background:linear-gradient(var(--orange),var(--orange-dark));
  display:flex;align-items:center;gap:20px;padding-left:30px;font-family:"Passion One",sans-serif;font-style:italic;font-size:14px;color:#111;text-transform:uppercase}
.search{left:779px;top:399px;width:136px;height:31px;border-radius:4px;border:2px solid #fff;background:#d8d8d8;
  display:flex;align-items:center;gap:8px;padding-left:10px;font-style:italic;font-size:12px;color:#555}
.panel{border:2px solid #fff;border-radius:3px;overflow:hidden;
  background:repeating-linear-gradient(135deg,#f2f2f2 0 3px,#d6d6d6 3px 4px)}
.panel-head{height:26px;display:flex;align-items:center;justify-content:center;font-family:"Exo 2",sans-serif;font-style:italic;font-weight:800;
  font-size:12px;color:#fff;text-transform:uppercase;background:linear-gradient(#555,var(--panel-dark))}
.panel-head.red{background:linear-gradient(#c22a00,var(--panel-red))}
.panel-head.green{background:linear-gradient(#35b520,var(--panel-green))}
.games{display:grid;grid-template-columns:repeat(4,82px);gap:15px;justify-content:center;padding-top:8px}
.game-card{text-align:center}
.thumb{width:82px;height:82px;border-radius:4px;background:var(--thumb);display:flex;align-items:center;justify-content:center;
  font-family:"Passion One",sans-serif;font-size:58px;color:#111}
.game-name{margin-top:9px;font-family:"Exo 2",sans-serif;font-style:italic;font-weight:800;font-size:11px;color:#555;letter-spacing:1px;text-transform:uppercase}
.tabs{display:flex;height:20px;background:linear-gradient(#fff,#ddd)}
.tab{flex:1;border-right:1px solid #bbb;font-size:9.5px;font-weight:500;color:#222;display:flex;align-items:center;justify-content:center;white-space:nowrap;overflow:hidden}
.tags{display:grid;grid-template-columns:repeat(5,66px);gap:10px 13px;justify-content:center;padding-top:10px}
.tag{height:22px;border-radius:4px;background:var(--tag)}
.recent{display:flex;gap:28px;padding:10px 0 0 10px;height:92px}
.recent .thumb{flex:none}
.recent-title{font-family:"Exo 2",sans-serif;font-style:italic;font-weight:800;font-size:11px;color:#555;letter-spacing:1px;text-transform:uppercase}
.recent-text{margin-top:8px;font-size:9px;font-style:italic;color:#666;line-height:1.25;text-transform:uppercase;width:128px}
.footer{left:0;top:1088px;width:1127px;display:flex;justify-content:center;font-family:"Montserrat",sans-serif;font-weight:600;font-size:13.5px;color:#fff;text-transform:uppercase}
.footer a{color:inherit;text-decoration:none;padding:6px 22px}
.footer a+a{border-left:2px solid #fff}
</style>
</head>
<body>
<div class="page-body"></div>

<header>
  <div class="abs logo">TOBIN-GAMES</div>
  <div class="abs btn" style="left:667px;top:38px">Login</div>
  <div class="abs btn" style="left:799px;top:38px">Signup</div>
</header>

<section class="abs slider" role="img" aria-label="Colourful illustration of cartoon game characters in a purple night scene">
  <div class="abs slider-panel">
    <div class="slider-title">NEW RELEASE</div>
    <p class="slider-text">"Lorem ipsum dolor sit amet, consectetur adipiscing elit, sed do eiusmod tempor incididunt ut labore et dolore magna aliqua. Ut enim ad minim veniam..."</p>
  </div>
  <div class="abs play">PLAY NOW</div>
  <svg class="abs" style="left:38px;top:101px" width="70" height="72" viewBox="0 0 70 72"><path d="M34 4 L4 36 L34 68 L34 50 L66 50 L66 22 L34 22 Z" fill="#f5b400" stroke="#fff" stroke-width="4" stroke-linejoin="round"/></svg>
  <svg class="abs" style="left:607px;top:101px" width="70" height="72" viewBox="0 0 70 72"><path d="M36 4 L66 36 L36 68 L36 50 L4 50 L4 22 L36 22 Z" fill="#f5b400" stroke="#fff" stroke-width="4" stroke-linejoin="round"/></svg>
  <div class="abs dot" style="left:249px"></div>
  <div class="abs dot" style="left:290px"></div>
  <div class="abs dot" style="left:331px"></div>
  <div class="abs dot active" style="left:373px"></div>
  <div class="abs dot" style="left:415px"></div>
  <div class="abs dot" style="left:456px"></div>
</section>

<nav class="abs nav">
  <span>Action</span><span>Casino</span><span>Adventure</span><span>Puzzle</span><span>Driving</span><span>Sports</span><span>Bubble</span>
</nav>
<div class="abs search">
  <svg width="16" height="16" viewBox="0 0 16 16"><circle cx="6" cy="6" r="4.5" fill="none" stroke="#222" stroke-width="2"/><line x1="9.5" y1="9.5" x2="15" y2="15" stroke="#222" stroke-width="2.5"/></svg>
  SEARCH HERE
</div>

<section class="abs panel" style="left:205px;top:451px;width:414px;height:152px">
  <div class="panel-head">Editor's Pick</div>
  <div class="games">
    <div class="game-card"><div class="thumb" role="img" aria-label="Game cover art in pink and purple" style="background:linear-gradient(135deg,#c23bd0,#3a6ad8)"></div><div class="game-name">Game #1</div></div>
    <div class="game-card"><div class="thumb" role="img" aria-label="Fantasy game cover art in warm orange tones" style="background:linear-gradient(135deg,#d8752a,#5a2410)"></div><div class="game-name">Game #2</div></div>
    <div class="game-card"><div class="thumb" role="img" aria-label="Strategy game cover art of ships at sea" style="background:linear-gradient(135deg,#6a8fb0,#8a6a50)"></div><div class="game-name">Game #3</div></div>
    <div class="game-card"><div class="thumb" role="img" aria-label="Adventure game cover art in deep blue" style="background:linear-gradient(135deg,#1f6a9a,#0d2b44)"></div><div class="game-name">Game #4</div></div>
  </div>
</section>

<section class="abs panel" style="left:205px;top:620px;width:414px;height:152px">
  <div class="panel-head red">Hot Games</div>
  <div class="games">
    <div class="game-card"><div class="thumb">?</div><div class="game-name">Game #1</div></div>
    <div class="game-card"><div class="thumb"></div><div class="game-name">Game #2</div></div>
    <div class="game-card"><div class="thumb"></div><div class="game-name">Game #3</div></div>
    <div class="game-card"><div class="thumb"></div><div class="game-name">Game #4</div></div>
  </div>
</section>

<section class="abs panel" style="left:205px;top:789px;width:414px;height:143px">
  <div class="tabs">
    <div class="tab">ACTION</div><div class="tab">CASINO</div><div class="tab">ADVENTURE</div><div class="tab">PUZZLE</div><div class="tab">DRIVING</div><div class="tab">SPORTS</div><div class="tab">BUBBLE</div>
  </div>
  <div class="games">
    <div class="game-card"><div class="thumb"></div><div class="game-name">Game #1</div></div>
    <div class="game-card"><div class="thumb"></div><div class="game-name">Game #2</div></div>
    <div class="game-card"><div class="thumb"></div><div class="game-name">Game #3</div></div>
    <div class="game-card"><div class="thumb"></div><div class="game-name">Game #4</div></div>
  </div>
</section>

<section class="abs panel" style="left:205px;top:949px;width:414px;height:100px">
  <div class="panel-head">Tags</div>
  <div class="tags">
    <div class="tag"></div><div class="tag"></div><div class="tag"></div><div class="tag"></div><div class="tag"></div>
    <div class="tag"></div><div class="tag"></div><div class="tag"></div><div class="tag"></div><div class="tag"></div>
  </div>
</section>

<section class="abs panel" style="left:636px;top:451px;width:277px;height:265px">
  <div class="panel-head">Game of the Day</div>
  <div class="abs" role="img" aria-label="Featured studio artwork for Kettlewick Games with a cyan stage and confetti" style="left:9px;top:37px;width:255px;height:214px;border-radius:10px;background:radial-gradient(circle at 50% 40%,#ffffff,#cfe6ef 60%,#9fb8c8)"></div>
</section>

<section class="abs panel" style="left:636px;top:736px;width:277px;height:313px">
  <div class="panel-head green">Recently Visited</div>
  <div class="recent"><div class="thumb"></div><div><div class="recent-title">Game #1</div><p class="recent-text">"Lorem ipsum dolor sit amet, consectetur adipiscing elit, sed do eiusmod tempor incididunt ut labore et»</p></div></div>
  <div class="recent"><div class="thumb"></div><div><div class="recent-title">Game #2</div><p class="recent-text">"Lorem ipsum dolor sit amet, consectetur adipiscing elit, sed do eiusmod tempor incididunt ut labore et»</p></div></div>
  <div class="recent"><div class="thumb"></div><div><div class="recent-title">Game #3</div><p class="recent-text">"Lorem ipsum dolor sit amet, consectetur adipiscing elit, sed do eiusmod tempor incididunt ut labore et»</p></div></div>
</section>

<footer class="abs footer">
  <a href="#">About Us</a><a href="#">Contact Us</a><a href="#">Terms &amp; Conditions</a>
</footer>
</body>
</html>
```